Brisk Tutorium Website

We are looking for a new design of our website. The current website is www.brisktutorium.example. The company is the #1 pre-college math and science program in Orange County, CA. We would like to see designs that integrate our logo with a modern color scheme. We are also open for suggestions that could improve our logo. We would like a simple, minimal, clean, classy, and vibrant front-page user interface design that give the premium, modern, innovative, creative, and premier brand feel. We like the "New Retro Colors for the Web" as described here: http://www.pixel-layoutnook.example/en/layout-notes-2013/.

Target Market(s)

The target market is parents with K-12 students from a diverse population. Parents are well educated with family income > $150,000. Most of the decision makers are mothers from immigrate families: 30% Chinese, 30% Korean, 15% Indian, 24% White.

Industry/Entity Type

College

Requirements
Must have
• Must read our statement of differentiation at:
• http://brisktutorium.example/about-us
• Your design must be reflective of your understanding of the statements.
Nice to have
• The design should also be mobil friendly.
Should not have
• While most of our current classes are math, our company is expanding to include STEM (Science, Technology, Engineering, and Math) for gifted students. Therefore, the site should not be JUST a math education site.

```html
<!DOCTYPE html>
<html lang="en">
<head>
<meta charset="utf-8">
<title>Brisk Tutorium for Gifted Youth</title>
<link href="https://fonts.googleapis.com/css2?family=Jost:wght@300;400;500&family=Arimo:wght@400;700&display=swap" rel="stylesheet">
<style>
:root{
  --blue:#3b8fd6;
  --blue-dark:#2a72b5;
  --green:#7ab834;
  --green-dark:#66a027;
  --ink:#333;
  --muted:#8a8a8a;
  --night:#2f3338;
  --night-2:#3a3d42;
  --night-3:#26292d;
  --paper:#fff;
  --line:#e6e6e6;
}
*{box-sizing:border-box;margin:0;padding:0}
html,body{width:894px;height:1200px;overflow:hidden}
body{position:relative;background:var(--paper);font-family:"Arimo",Arial,sans-serif;color:var(--ink)}
.abs{position:absolute}
.head{font-family:"Jost",Arial,sans-serif;font-weight:300}

/* top */
.topbar{left:0;top:0;width:894px;height:24px;background:var(--night)}
.topbar-inner{left:138px;top:0;width:617px;height:24px;background:#f2f2f2}
.toplinks{right:98px;top:7px;font-size:7.5px;color:#888}
.login{left:683px;top:3px;width:58px;height:16px;background:var(--blue);color:#fff;font-size:8px;text-align:center;line-height:16px}
.band-left{left:0;top:24px;width:138px;height:103px;background:var(--blue)}
.band-right{left:755px;top:24px;width:139px;height:92px;background:var(--night)}
.masthead{left:138px;top:24px;width:617px;height:55px;background:#fff}
.brand{left:16px;top:18px;display:flex;align-items:center;gap:7px;font-family:"Jost",sans-serif;font-size:19px;color:var(--blue);font-weight:400}
.brand i{width:18px;height:18px;border-radius:50%;background:var(--green);display:block}
.nav{left:212px;top:0;height:55px;display:flex;gap:0;font-size:9px;color:#777}
.nav a{display:block;padding:27px 11.5px 0;height:55px;color:#777;text-decoration:none}
.nav a.active{color:var(--blue);border-top:2px solid var(--blue);padding-top:25px}
.strip{left:138px;top:79px;width:617px;height:37px;background:var(--night)}
.contact-tab{left:0;top:0;height:37px}
.phone{left:15px;top:8px;color:#fff;font-size:12.5px;display:flex;align-items:center;gap:6px}
.mail{left:15px;top:25px;color:#fff;font-size:8.5px;display:flex;align-items:center;gap:6px}
.search{left:430px;top:9px;width:171px;height:20px;background:#3f4348;color:#bbb;font-size:8px;line-height:20px;padding-left:7px}
.search svg{position:absolute;right:6px;top:4px}

/* hero */
.hero{left:138px;top:116px;width:617px;height:258px;background:linear-gradient(135deg,#6d4a3e 0%,#a88f78 35%,#cdbfae 60%,#7a6d63 100%)}
.hero h2{position:absolute;left:0;right:0;top:117px;text-align:center;font-family:"Jost",sans-serif;font-weight:300;color:#fff;font-size:18px}
.hero p{position:absolute;left:118px;right:118px;top:148px;text-align:center;color:#fff;font-size:8.5px;line-height:11px}
.dots{left:286px;top:234px;display:flex;gap:4px}
.dots span{width:7px;height:7px;border-radius:50%;background:#fff}
.dots span.on{background:var(--blue);box-shadow:0 0 0 1.5px #fff}

/* welcome */
.welcome-title{left:138px;width:617px;top:399px;text-align:center;font-size:17px;color:#333}
.welcome-text{left:148px;width:597px;top:432px;text-align:center;font-size:7.5px;line-height:11.5px;color:var(--muted)}
.btn-blue{left:393px;top:480px;width:107px;height:22px;background:var(--blue);border-bottom:2px solid var(--blue-dark);color:#fff;font-size:10px;text-align:center;line-height:21px}
.rule{left:195px;width:505px;height:1px;background:linear-gradient(90deg,transparent,var(--line),transparent)}

/* stem */
.stem{width:140px;text-align:center}
.stem .ring{width:80px;height:80px;border-radius:50%;margin:0 auto;background:#f2f2f2;box-shadow:3px 4px 6px rgba(0,0,0,.12);display:flex;align-items:center;justify-content:center}
.stem .ring b{width:64px;height:64px;border-radius:50%;background:var(--green);display:flex;align-items:center;justify-content:center}
.stem h3{font-family:"Jost",sans-serif;font-weight:300;font-size:13px;margin-top:13px;color:#333}
.stem p{font-size:7.5px;line-height:11px;color:var(--muted);margin-top:7px;padding:0 2px}
.stem .btn{width:81px;height:21px;margin:11px auto 0;background:#45484c;border-bottom:2px solid #2c2e31;color:#fff;font-size:8.5px;line-height:20px}

/* events */
.events-title{left:138px;top:762px;font-size:15px;color:#333}
.event-photo{left:138px;top:792px;width:186px;height:67px;background:linear-gradient(120deg,#5b6b3d,#b79a86 45%,#6f7894 75%,#9a8f87)}
.event-info{left:335px;top:791px;width:190px;font-size:7.5px;line-height:11px;color:#444}
.event-info .when{color:var(--green);margin-top:2px}
.event-info .sub{margin-top:3px}
.event-info .muted{color:var(--muted);margin-top:4px}
.event-desc{left:138px;top:869px;width:385px;font-size:7.5px;line-height:11px;color:var(--muted)}
.share{left:138px;top:906px;font-size:7.5px;color:var(--blue);display:flex;align-items:center;gap:5px}
.share i{width:6px;height:6px;border:1px solid #aaa;display:block}

/* calendar */
.cal{left:598px;top:766px;width:157px}
.cal-head{height:19px;background:#45484c;color:#fff;font-family:"Jost",sans-serif;font-size:10px;text-align:center;line-height:19px;position:relative}
.cal-head span{position:absolute;top:0;width:20px;height:19px;background:#3a3d41}
.cal-head .prev{left:0}.cal-head .next{right:0;background:#5b5e62}
.cal table{width:157px;border-collapse:collapse;table-layout:fixed}
.cal th{background:var(--green);color:#fff;font-size:6px;height:16px;font-weight:700}
.cal td{height:22px;text-align:center;font-size:8px;font-weight:700;color:#444;background:#f3f3f3;border:1px solid #fff}
.cal td.out{color:#bbb;background:#f8f8f8}
.cal td.today{color:var(--green)}
.cal td.ev{position:relative}
.tag{position:absolute;left:42px;top:814px;width:32px;height:12px;background:var(--green);color:#fff;font-size:6px;font-weight:700;text-align:center;line-height:12px}

/* newsletter */
.news-dark{left:0;top:973px;width:894px;height:48px;background:var(--night)}
.news-blue{left:480px;top:962px;width:414px;height:103px;background:var(--blue);clip-path:polygon(36px 0,100% 0,100% 100%,0 100%,0 59px,8px 59px)}
.news-icon{left:153px;top:987px}
.news-text{left:204px;top:988px;width:275px;font-size:7.5px;line-height:11px;color:#999}
.news-badge{left:518px;top:973px;width:36px;height:36px;border-radius:50%;background:#2b75b8;border:2px solid #6aa9e0;display:flex;align-items:center;justify-content:center}
.news-title{left:570px;top:970px;color:#fff;font-family:"Jost",sans-serif;font-size:12px}
.news-input{left:570px;top:991px;width:140px;height:18px;background:#1f5e97;color:#e0ecf7;font-size:7.5px;line-height:18px;padding-left:7px}
.news-go{left:716px;top:991px;width:25px;height:18px;background:#2b75b8;color:#fff;font-size:7.5px;text-align:center;line-height:18px}

/* footer */
.foot-bg{left:0;top:1021px;width:894px;height:179px;background:var(--night-3)}
.foot-left{left:0;top:1021px;width:138px;height:44px;background:var(--night)}
.foot{left:138px;top:1021px;width:617px;height:179px;background:var(--night-2)}
.foot-brand{left:16px;top:68px;width:150px;text-align:center;color:#fff;font-family:"Jost",sans-serif;font-size:16px}
.foot-brand i{display:block;width:34px;height:34px;border-radius:50%;background:#fff;margin:0 auto 10px}
.foot h4{position:absolute;top:25px;color:#fff;font-family:"Jost",sans-serif;font-weight:400;font-size:10px}
.foot ul{position:absolute;top:52px;list-style:none;font-size:7.5px;color:#999}
.foot li{margin-bottom:11px;padding-left:12px;position:relative}
.foot li:before{content:"";position:absolute;left:0;top:3px;width:4px;height:4px;border-radius:50%;background:#777}
.foot .col-txt{position:absolute;font-size:7.5px;line-height:11px;color:#999}
.socials{display:flex;gap:7px;position:absolute}
.socials span{width:14px;height:14px;border-radius:50%;background:#5b5e62;display:block}
.contact-row{position:absolute;display:flex;gap:8px;font-size:7.5px;line-height:11px;color:#999}
.foot-rule{left:12px;top:147px;width:593px;height:1px;background:#4d5055}
.copy{left:0;width:617px;top:160px;text-align:center;font-size:7.5px;color:#999}
.copy span{color:var(--blue)}
</style>
</head>
<body>

<div class="abs topbar"></div>
<div class="abs topbar-inner">
  <div class="abs toplinks">About Us &nbsp;/&nbsp; Blog &nbsp;/&nbsp; Contact Us</div>
  <div class="abs login">Log In</div>
</div>

<div class="abs band-left"></div>
<div class="abs band-right"></div>

<header class="abs masthead">
  <div class="abs brand"><i></i>Brisk Tutorium</div>
  <nav class="abs nav">
    <a class="active">Home</a><a>Admission</a><a>Academics</a><a>Courses</a><a>News / Events</a><a>Results</a><a>Fall 2013</a>
  </nav>
</header>

<div class="abs strip">
  <svg class="abs contact-tab" width="210" height="37" viewBox="0 0 210 37"><polygon points="0,0 210,0 180,37 0,37" fill="#3b8fd6"/></svg>
  <div class="abs phone">
    <svg width="16" height="16" viewBox="0 0 16 16"><circle cx="8" cy="8" r="7" fill="none" stroke="#fff" stroke-width="1.2"/><path d="M6 4.5c-1 .6-1.2 2-.3 3.8s2 2.8 3.2 3.2c.6.2 1.1-.2 1.4-.6l-1.2-1.3-.9.4c-.6-.4-1.2-1.2-1.5-2l.7-.7L6.8 5z" fill="#fff"/></svg>
    (555) 014-2211
  </div>
  <div class="abs mail">
    <svg width="14" height="9" viewBox="0 0 14 9"><rect width="14" height="9" fill="#fff"/><path d="M0 0l7 5 7-5" fill="none" stroke="#3b8fd6" stroke-width="1"/></svg>
    info@brisktutorium.example
  </div>
  <div class="abs search">Search...
    <svg width="12" height="12" viewBox="0 0 12 12"><circle cx="7" cy="5" r="3.8" fill="none" stroke="#ddd" stroke-width="1.4"/><path d="M4.3 7.7L1 11" stroke="#ddd" stroke-width="1.6"/></svg>
  </div>
</div>

<section class="abs hero" role="img" aria-label="Photo of students studying at a library table">
  <h2>Lorem ipsum dolor sit amet, consectetur adipiscing elit.</h2>
  <p>Donec laoreet fringilla fermentum. In porta posuere vestibulum. Quisque congue, lorem id aliquet dignissim, mauris massa tempor felis, id porttitor turpis lectus ac nulla. Duis at porttitor tortor. Praesent imperdiet ullamcorper felis, eget iaculis tortor ornare sit amet.</p>
  <div class="abs dots"><span class="on"></span><span></span><span></span><span></span></div>
</section>

<h1 class="abs head welcome-title">Welcome to Brisk Tutorium For Gifted Youth</h1>
<p class="abs welcome-text">Lorem ipsum dolor sit amet, consectetur adipiscing elit. Mauris sit amet quam nunc. Aliquam suscipit rutrum orci in convallis. Proin neque nunc, placerat ut pellentesque id, scelerisque vel nulla. Donec condimentum enim eu scelerisque hendrerit. Cras ornare vehicula purus. Aenean rutrum, arcu eu tristique volutpat, sapien quam vulputate justo, sed bibendum massa mi nec turpis. Ut ornare, sapien ultricies eleifend porttitor, velit nisl ullamcorper felis, eu fringilla enim justo vel nunc.</p>
<div class="abs btn-blue">Lean More</div>
<div class="abs rule" style="top:519px"></div>

<div class="abs stem" style="left:133px;top:537px">
  <div class="ring"><b><svg width="30" height="30" viewBox="0 0 30 30" fill="none" stroke="#fff" stroke-width="1.8"><path d="M11 6h8M13 6v7l-6 11h16l-6-11V6" transform="rotate(30 15 15)"/><circle cx="22" cy="6" r="2"/></svg></b></div>
  <h3>Science</h3>
  <p>Sed lobortis commodo nulla ut congue. mollis, neque in fringilla luctus, nunc ipsum, a congue ante id nunc.</p>
  <div class="btn">Lean More</div>
</div>
<div class="abs stem" style="left:295px;top:537px">
  <div class="ring"><b><svg width="28" height="26" viewBox="0 0 28 26" fill="none" stroke="#fff" stroke-width="2"><rect x="3" y="3" width="22" height="14" rx="1"/><path d="M14 17v5M9 23h10"/></svg></b></div>
  <h3>Technology</h3>
  <p>Sed lobortis commodo nulla ut congue. mollis, neque in fringilla luctus, nunc ipsum, a congue ante id nunc.</p>
  <div class="btn">Lean More</div>
</div>
<div class="abs stem" style="left:459px;top:537px">
  <div class="ring"><b><svg width="30" height="30" viewBox="0 0 30 30" fill="none" stroke="#fff" stroke-width="2.2"><circle cx="10" cy="20" r="4" stroke-dasharray="2.5 1.5"/><circle cx="19" cy="10" r="4.5" stroke-dasharray="2.5 1.5"/><circle cx="25" cy="5" r="2"/></svg></b></div>
  <h3>Engineering</h3>
  <p>Sed lobortis commodo nulla ut congue. mollis, neque in fringilla luctus, nunc ipsum, a congue ante id nunc.</p>
  <div class="btn">Lean More</div>
</div>
<div class="abs stem" style="left:621px;top:537px">
  <div class="ring"><b><svg width="30" height="28" viewBox="0 0 30 28"><path d="M3 16l3-2 4 9 5-20h12" fill="none" stroke="#fff" stroke-width="2"/><text x="21" y="13" font-size="8" fill="#fff" font-family="Arimo" font-style="italic">x</text><path d="M17 15h10" stroke="#fff" stroke-width="1.2"/><text x="21" y="23" font-size="8" fill="#fff" font-family="Arimo" font-style="italic">y</text></svg></b></div>
  <h3>Math</h3>
  <p>Sed lobortis commodo nulla ut congue. mollis, neque in fringilla luctus, nunc ipsum, a congue ante id nunc.</p>
  <div class="btn">Lean More</div>
</div>

<div class="abs rule" style="top:742px"></div>

<h2 class="abs head events-title">Upcoming Events</h2>
<div class="abs event-photo" role="img" aria-label="Photo of students gathered at an outdoor campus event"></div>
<div class="abs event-info">
  <div>Lorem ipsum dolor sit amet, consectetur adipiscing elit.</div>
  <div class="when">MATH CLASS Monday, September 15, 11 AM.</div>
  <div class="sub">Lorem ipsum dolor sit amet elit.</div>
  <div class="muted">Sed lobortis commodo nulla ut congue. Fusce mollis, neque in fringilla luctus, nunc ante scelerisque ipsum, a congue urna ante id nunc.</div>
</div>
<p class="abs event-desc">Aliquam id magna vel nibh facilisis aliquet. Vestibulum in orci nisl. Maecenas elit nisl, suscipit vitae semper vitae, tempus eu elit. Phasellus leo felis, egestas et purus a, lobortis commodo nulla. Nam nec metus ullamcorper, malesuada dolor quis, tristique augue.</p>
<div class="abs share"><i></i>Share this event</div>

<div class="abs cal">
  <div class="cal-head">
    <span class="prev"><svg width="20" height="19" viewBox="0 0 20 19"><path d="M12 6l-4 3.5 4 3.5" fill="none" stroke="#fff" stroke-width="2"/></svg></span>
    September 2013
    <span class="next"><svg width="20" height="19" viewBox="0 0 20 19"><path d="M8 6l4 3.5-4 3.5" fill="none" stroke="#fff" stroke-width="2"/></svg></span>
  </div>
  <table>
    <tr><th>SUN</th><th>MON</th><th>TUE</th><th>WED</th><th>THU</th><th>FRI</th><th>SAT</th></tr>
    <tr><td>1</td><td>2</td><td>3</td><td>4</td><td>5</td><td>6</td><td>7</td></tr>
    <tr><td>8</td><td>9</td><td class="ev">10</td><td>11</td><td>12</td><td>13</td><td>14</td></tr>
    <tr><td>15</td><td>16</td><td>17</td><td>18</td><td>19</td><td class="today">20</td><td>21</td></tr>
    <tr><td>22</td><td>23</td><td>24</td><td>25</td><td>26</td><td>27</td><td>28</td></tr>
    <tr><td>29</td><td>30</td><td>31</td><td class="out">1</td><td class="out">2</td><td class="out">3</td><td class="out">4</td></tr>
  </table>
</div>
<div class="abs tag" style="left:637px">EVENT</div>

<div class="abs foot-bg"></div>
<div class="abs news-dark"></div>
<div class="abs news-blue"></div>
<svg class="abs news-icon" width="26" height="20" viewBox="0 0 26 20" fill="none" stroke="#bbb" stroke-width="1.3"><rect x="3" y="2" width="21" height="16"/><path d="M3 6H1v11a1 1 0 0 0 2 1M6 6h7v5H6zM15 6h6M15 9h6M6 14h15"/></svg>
<p class="abs news-text">Lorem ipsum dolor sit amet, consectetur adipiscing elit. Mauris sit amet quam nunc. Aliquam suscipit rutrum orci in convallis.</p>
<div class="abs news-badge"><svg width="18" height="14" viewBox="0 0 18 14" fill="none" stroke="#fff" stroke-width="1.4"><path d="M1 6l8-5 8 5v7H1z"/><path d="M1 6l8 5 8-5"/></svg></div>
<div class="abs news-title">Newsletter Sign Up</div>
<div class="abs news-input">your email address</div>
<div class="abs news-go">Go</div>

<div class="abs foot-left"></div>
<footer class="abs foot">
  <div class="abs foot-brand"><i></i>Brisk Tutorium</div>

  <h4 style="left:174px">Courses Offer</h4>
  <ul style="left:174px"><li>Science Courses</li><li>Technology Courses</li><li>Engineering Courses</li><li>Math Courses</li></ul>

  <h4 style="left:312px">Stay In Touch</h4>
  <p class="col-txt" style="left:312px;top:54px;width:125px">Follow Us in our social networks! Lorem ipsum dolor sit amet, consectetur adipiscing elit.</p>
  <div class="socials" style="left:312px;top:99px"><span></span><span></span><span></span><span></span></div>

  <h4 style="left:484px">Contact Us</h4>
  <div class="contact-row" style="left:484px;top:54px">
    <svg width="7" height="10" viewBox="0 0 7 10"><path d="M3.5 0A3.5 3.5 0 0 0 0 3.5C0 6 3.5 10 3.5 10S7 6 7 3.5A3.5 3.5 0 0 0 3.5 0z" fill="#888"/></svg>
    <span>2200 Harbor Lane, Suite 140<br>Irvine, CA 92600-0000</span>
  </div>
  <div class="contact-row" style="left:484px;top:88px">
    <svg width="8" height="8" viewBox="0 0 8 8"><path d="M1 .5c-1 1-.8 3 1 5s4 2.3 5 1.5L5.5 5.3 4.5 6C3.5 5.5 2.5 4.5 2 3.5l.7-1L1 .5z" fill="#888"/></svg>
    <span>(555) 014-2211</span>
  </div>
  <div class="contact-row" style="left:484px;top:108px">
    <svg width="9" height="7" viewBox="0 0 9 7"><rect width="9" height="7" fill="#888"/><path d="M0 0l4.5 3.5L9 0" fill="none" stroke="#3a3d42"/></svg>
    <span>info@brisktutorium.example</span>
  </div>

  <div class="abs foot-rule"></div>
  <div class="abs copy">Copyright © 2000-2013 , <span>Brisk Tutorium</span> for Gifted Youth</div>
</footer>

</body>
</html>
```